Plovenworks business card

We need a modern business card - With our 4 colors - See web: www.plovenworks.dk

I have attached logo and som old business Cards we have - Lets Make the new ones shine...:-) -

Industry/Entity Type

Business

Requirements
Must have
• the logo with plovnworks only,

```html
<!DOCTYPE html>
<html lang="da">
<head>
<meta charset="utf-8">
<title>Plovenworks business card</title>
<link rel="stylesheet" href="https://fonts.googleapis.com/css2?family=Source+Sans+3:wght@400;600&display=swap">
<style>
  :root {
    --bg: #e4e4e4;
    --card: #ffffff;
    --green: #8cc65b;
    --purple: #6b2a75;
    --pink: #c9318a;
    --orange: #e38a3f;
    --ink: #555555;
    --rule: #333333;
  }
  * { margin: 0; padding: 0; box-sizing: border-box; }
  html, body { width: 1105px; height: 1200px; overflow: hidden; }
  body {
    background: var(--bg);
    font-family: "Source Sans 3", "Myriad Pro", sans-serif;
    color: var(--ink);
    position: relative;
  }
  .card {
    position: absolute;
    left: 192px;
    width: 720px;
    height: 412px;
    border-radius: 22px;
    overflow: hidden;
  }
  .card-front { top: 150px; background: var(--card); }
  .card-back { top: 607px; display: flex; }

  .brand {
    position: absolute;
    top: 128px; left: 0; right: 0;
    display: flex; justify-content: center; align-items: center; gap: 12px;
  }
  .brand-dot { width: 28px; height: 28px; border-radius: 50%; background: var(--green); }
  .brand-name { font-size: 32px; font-weight: 400; color: #3a3a3a; letter-spacing: 1px; }
  .brand-rule {
    position: absolute; top: 186px; left: 240px; width: 242px; height: 2px; background: var(--green);
  }
  .tagline {
    position: absolute; top: 200px; left: 0; right: 0; text-align: center;
    font-size: 15px; color: #444;
  }
  .person-name {
    position: absolute; top: 242px; left: 0; right: 0; text-align: center;
    font-size: 26px; font-weight: 600; color: var(--green);
  }
  .title-row {
    position: absolute; top: 278px; left: 36px; right: 40px;
    display: flex; align-items: center; gap: 8px;
  }
  .title-row::before, .title-row::after { content: ""; flex: 1; height: 1px; background: var(--rule); }
  .job-title { font-size: 19px; color: #333; }

  .contacts { position: absolute; top: 301px; left: 36px; list-style: none; }
  .contacts li { display: flex; align-items: center; gap: 14px; height: 28px; font-size: 19px; }
  .contacts svg { width: 18px; height: 18px; fill: var(--green); }
  .address {
    position: absolute; top: 301px; right: 33px; text-align: right;
    font-style: normal; font-size: 19px; line-height: 28px;
  }

  .stripe { height: 100%; }
  .stripe-green { width: 24.4%; background: var(--green); }
  .stripe-purple { width: 24.6%; background: var(--purple); }
  .stripe-pink { width: 25.5%; background: var(--pink); }
  .stripe-orange { width: 25.5%; background: var(--orange); }
  .back-brand {
    position: absolute; inset: 0; display: flex; align-items: center; justify-content: center;
    font-size: 52px; font-weight: 400; color: #ffffff; letter-spacing: 2px;
  }
</style>
</head>
<body>
  <section class="card card-front">
    <div class="brand">
      <span class="brand-dot"></span>
      <span class="brand-name">plovnworks</span>
    </div>
    <div class="brand-rule"></div>
    <p class="tagline">ideer der holder</p>
    <h1 class="person-name">Mads Terkelsen</h1>
    <div class="title-row"><span class="job-title">Salgsdirektør</span></div>
    <ul class="contacts">
      <li><svg viewBox="0 0 24 24"><path d="M6.6 10.8a15.1 15.1 0 0 0 6.6 6.6l2.2-2.2c.3-.3.7-.4 1-.2 1.1.4 2.3.6 3.6.6.6 0 1 .4 1 1V20c0 .6-.4 1-1 1A17 17 0 0 1 3 4c0-.6.4-1 1-1h3.5c.6 0 1 .4 1 1 0 1.3.2 2.5.6 3.6.1.3 0 .7-.2 1z"/></svg>+45 31 72 40 18</li>
      <li><svg viewBox="0 0 24 24"><path d="M6.6 10.8a15.1 15.1 0 0 0 6.6 6.6l2.2-2.2c.3-.3.7-.4 1-.2 1.1.4 2.3.6 3.6.6.6 0 1 .4 1 1V20c0 .6-.4 1-1 1A17 17 0 0 1 3 4c0-.6.4-1 1-1h3.5c.6 0 1 .4 1 1 0 1.3.2 2.5.6 3.6.1.3 0 .7-.2 1z"/></svg>+45 52 63 14 87</li>
      <li><svg viewBox="0 0 24 24"><path d="M2 5h20v14H2z M2 5l10 8 10-8" stroke="#fff" stroke-width="1.5"/></svg>mt@plovenworks.dk</li>
    </ul>
    <address class="address">
      Kastanjegade 14<br>
      8600 Silkeborg<br>
      www.plovenworks.dk
    </address>
  </section>

  <section class="card card-back">
    <div class="stripe stripe-green"></div>
    <div class="stripe stripe-purple"></div>
    <div class="stripe stripe-pink"></div>
    <div class="stripe stripe-orange"></div>
    <div class="back-brand">plovnworks</div>
  </section>
</body>
</html>
```